K7 Digital Stationery Design Project

We are looking to have stationary designs created for our company branding materials. We are looking for the following to be created.
1. Business Cards (front & back)
2. Letterhead
3. Envelopes #10
We are a new web design, development and marketing firm. Primary color scheme is desired to be blue/grey/white. This web start-up is owned and operated by individuals with 15+ years experience each in the industry so should not look as though it is a start-up by young/inexperienced individuals.
We build website & custom applications/software. In addition we provide the full spectrum of web marketing solutions including SEO, PPC, Social Media, Branding, Content Marketing and PR.
Please let us know if you have any questions. Looking forward to seeing all the amazing design ideas.
Attached is our logo.
Thanks!
Target Market(s)
Company will be nearly 100% business to business sales. Looking to work with companies that are already established, with a website, who want to take their website and/or online marketing efforts to the next level.
Industry/Entity Type
Marketing
Look and feel

```html
<!DOCTYPE html>
<html lang="en">
<head>
<meta charset="utf-8">
<title>K7 Digital Stationery</title>
<link rel="stylesheet" href="https://fonts.googleapis.com/css2?family=Jost:wght@400;500;700&display=swap">
<style>
:root{
  --bg:#e9ebee;
  --paper:#ffffff;
  --ink:#2b2b2b;
  --ink-soft:#555a60;
  --blue:#1b8fd2;
  --blue-deep:#0b6fb3;
  --blue-light:#39b1ea;
  --grey:#8f959b;
  --grey-light:#c9cdd1;
  --charcoal:#3a3b3d;
  --shadow:0 3px 10px rgba(0,0,0,.18);
}
*{box-sizing:border-box;margin:0;padding:0}
html,body{width:1200px;height:808px;overflow:hidden}
body{background:var(--bg);font-family:"Jost",sans-serif;color:var(--ink);position:relative}
.piece{position:absolute;background:var(--paper);box-shadow:var(--shadow);overflow:hidden}
.wave{position:absolute;left:0;bottom:0;width:100%;display:block}
.brand{font-family:"Jost",sans-serif;font-weight:700;color:var(--blue);letter-spacing:.2px;line-height:1;display:flex;align-items:center;gap:6px}
.brand-dot{display:inline-block;border-radius:50%;background:currentColor}
.tagline{font-size:7px;color:var(--ink-soft);margin-top:3px;letter-spacing:.2px}
.contact{position:absolute;color:#fff;font-size:7.5px;line-height:1.45;letter-spacing:.2px;z-index:1}
.contact .url{letter-spacing:2px;font-size:8px}
.icon{display:inline-block;vertical-align:-1px;margin-right:2px}

/* Letterhead */
.letterhead{left:20px;top:24px;width:588px;height:760px}
.letterhead .brand-block{position:absolute;right:60px;top:62px;text-align:left}
.letterhead .brand{font-size:22px}
.letterhead .brand-dot{width:12px;height:12px}
.letterhead .tagline{font-size:8.5px}
.letter{position:absolute;left:44px;top:146px;width:505px;font-size:11px;line-height:1.45;color:var(--ink);z-index:1}
.letter .date{margin-bottom:12px}
.recipient-name{font-weight:700;font-size:12.5px}
.recipient-role{margin-bottom:10px}
.recipient-company{font-weight:500}
.letter p{margin-top:12px;text-align:left;font-size:10.5px;line-height:1.5}
.signature{display:block;height:34px;margin-top:10px}
.signer{font-weight:700;font-size:12px;margin-top:4px}
.letterhead .contact{left:44px;bottom:22px;font-size:8px}

/* Business cards */
.card{width:265px;height:151px;top:24px}
.card-front{left:640px}
.card-back{left:915px;background:linear-gradient(160deg,var(--blue-light),var(--blue-deep))}
.card-front .holder{position:absolute;left:18px;top:24px}
.holder-name{color:var(--blue);font-size:12px;font-weight:500}
.holder-role{font-size:8px;color:var(--ink-soft);margin-top:1px}
.card-front .brand-block{position:absolute;right:16px;top:30px}
.card .brand{font-size:14px}
.card .brand-dot{width:7px;height:7px}
.card .tagline{font-size:5.5px}
.card-front .contact{left:16px;bottom:10px;font-size:6.5px}
.card-front .web{position:absolute;right:18px;bottom:12px;color:#fff;font-size:6.5px;letter-spacing:.5px}
.card-back .brand-block{position:absolute;left:118px;top:46px}
.card-back .brand,.card-back .tagline{color:#fff}
.card-back .web{position:absolute;left:20px;bottom:14px;color:#dfe3e6;font-size:6.5px;letter-spacing:.5px}

/* Envelope front */
.envelope-front{left:640px;top:195px;width:540px;height:234px}
.envelope-front .brand-block{position:absolute;left:30px;top:52px}
.envelope-front .brand{font-size:18px}
.envelope-front .brand-dot{width:10px;height:10px}
.envelope-front .tagline{font-size:7px}
.address-lines{position:absolute;left:250px;top:42px;width:210px}
.address-lines span{display:block;height:1px;background:var(--grey-light);margin-bottom:28px}
.envelope-front .contact{left:30px;bottom:16px;font-size:7.5px}

/* Envelope back */
.envelope-back{left:640px;top:449px;width:540px;height:234px;background:#f6f7f8}
.envelope-back .folds{position:absolute;inset:0;width:100%;height:100%}
.envelope-back .flap{position:absolute;left:0;top:0;width:100%;height:120px}
.envelope-back .brand-block{position:absolute;left:0;right:0;top:34px;display:flex;justify-content:center}
.envelope-back .brand{font-size:15px;color:#fff}
.envelope-back .brand-dot{width:8px;height:8px}
</style>
</head>
<body>

<!-- Letterhead -->
<section class="piece letterhead" aria-label="Letterhead">
  <div class="brand-block">
    <div class="brand"><span class="brand-dot"></span>K7 Digital</div>
    <div class="tagline">Web Design, Development and Marketing</div>
  </div>
  <div class="letter">
    <div class="date">January 15, 2011</div>
    <div class="recipient-name">Mr Peter Lindqvist</div>
    <div class="recipient-role">Director of Operation</div>
    <div class="recipient-company">Northgate Holdings</div>
    <div>250 W Harbor Road</div>
    <div>Tallow Bay, WA 98610</div>
    <p>Lorem Ipsum is simply dummy text of the printing and typesetting industry. Lorem Ipsum has been the industry's standard dummy text ever since the 1500s, when an unknown printer took a galley of type and scrambled it to make a type specimen book. It has survived not only five centuries, but also the leap into electronic typesetting, remaining essentially unchanged. It was popularised in the 1960s with the release of Printrite sheets containing Lorem Ipsum passages, and more recently with desktop publishing software like Pagecraft including versions of Lorem Ipsum.</p>
    <p>Contrary to popular belief, Lorem Ipsum is not simply random text. It has roots in a piece of classical Latin literature from 45 BC, making it over 2000 years old. Daniel Ferrow, a Latin professor at Harlow College in Virginia, looked up one of the more obscure Latin words, consectetur, from a Lorem Ipsum passage, and going through the cites of the word in classical literature, discovered the undoubtable source. Lorem Ipsum comes from sections 1.10.32 and 1.10.33 of "de Finibus Bonorum et Malorum" (The Extremes of Good and Evil) by Calvinus, written in 45 BC. This book is a treatise on the theory of ethics, very popular during the Renaissance. The first line of Lorem Ipsum, "Lorem ipsum dolor sit amet..", comes from a line in section 1.10.32.</p>
    <p>Thank You for being one of our valued customers.</p>
    <svg class="signature" viewBox="0 0 160 40" width="136" aria-hidden="true">
      <path d="M6 30 C10 8,22 6,20 22 C18 34,8 32,14 18 C20 6,34 10,30 24 C28 30,36 22,42 20 C48 18,46 28,52 24 C70 14,110 12,150 10" fill="none" stroke="#222" stroke-width="1.3"/>
    </svg>
    <div class="signer">Milan Doroshev</div>
    <div>President</div>
    <div>Tallow Bay Fabrication</div>
  </div>
  <svg class="wave" viewBox="0 0 588 110" height="110" preserveAspectRatio="none" aria-hidden="true">
    <defs>
      <linearGradient id="lhBlue" x1="0" y1="0" x2="1" y2="0">
        <stop offset="0" stop-color="#0b6fb3"/><stop offset=".5" stop-color="#1b8fd2"/><stop offset="1" stop-color="#39b1ea"/>
      </linearGradient>
    </defs>
    <path d="M0 34 C160 8,330 70,588 14 L588 30 C330 80,160 20,0 46Z" fill="#9aa0a6"/>
    <path d="M0 46 C160 20,330 84,588 28 L588 110 L0 110Z" fill="url(#lhBlue)"/>
  </svg>
  <div class="contact">
    1876 N. 52nd Court Linden, NE 68420<br>
    <svg class="icon" width="8" height="8" viewBox="0 0 10 10" aria-hidden="true"><path d="M2 1h2l1 2-1 1c.5 1 1 1.5 2 2l1-1 2 1v2c-4 0-7-3-7-7z" fill="#fff"/></svg>+1 55 210-4836
    <svg class="icon" width="9" height="7" viewBox="0 0 10 8" aria-hidden="true"><rect x=".5" y=".5" width="9" height="7" fill="none" stroke="#fff"/><path d="M.5 .5 5 4.5 9.5 .5" fill="none" stroke="#fff"/></svg>hello@k7digital.net<br>
    <span class="url">www.k7digital.net</span>
  </div>
</section>

<!-- Business card front -->
<section class="piece card card-front" aria-label="Business card front">
  <div class="holder">
    <div class="holder-name">Owen Carradine</div>
    <div class="holder-role">Position</div>
  </div>
  <div class="brand-block">
    <div class="brand"><span class="brand-dot"></span>K7 Digital</div>
    <div class="tagline">Web Design, Development and Marketing</div>
  </div>
  <svg class="wave" viewBox="0 0 265 80" height="80" preserveAspectRatio="none" aria-hidden="true">
    <defs>
      <linearGradient id="cfBlue" x1="0" y1="0" x2="1" y2="0">
        <stop offset="0" stop-color="#0b6fb3"/><stop offset=".6" stop-color="#1b8fd2"/><stop offset="1" stop-color="#39b1ea"/>
      </linearGradient>
    </defs>
    <path d="M0 26 C80 6,160 40,265 4 L265 14 C160 50,80 16,0 34Z" fill="#9aa0a6"/>
    <path d="M0 34 C80 16,160 52,265 14 L265 80 L0 80Z" fill="url(#cfBlue)"/>
  </svg>
  <div class="contact">
    1876 N. 52nd Court<br>Linden, NE 68420<br>
    +1 55 210-4836<br>hello@k7digital.net
  </div>
  <div class="web">www.k7digital.net</div>
</section>

<!-- Business card back -->
<section class="piece card card-back" aria-label="Business card back">
  <div class="brand-block">
    <div class="brand"><span class="brand-dot"></span>K7 Digital</div>
    <div class="tagline">Web Design, Development and Marketing</div>
  </div>
  <svg class="wave" viewBox="0 0 265 60" height="60" preserveAspectRatio="none" aria-hidden="true">
    <path d="M0 14 C90 -2,170 30,265 6 L265 16 C170 40,90 8,0 24Z" fill="#b8bdc2"/>
    <path d="M0 24 C90 8,170 40,265 16 L265 60 L0 60Z" fill="#3a3b3d"/>
  </svg>
  <div class="web">www.k7digital.net</div>
</section>

<!-- Envelope front -->
<section class="piece envelope-front" aria-label="Envelope front">
  <div class="brand-block">
    <div class="brand"><span class="brand-dot"></span>K7 Digital</div>
    <div class="tagline">Web Design, Development and Marketing</div>
  </div>
  <div class="address-lines"><span></span><span></span><span></span></div>
  <svg class="wave" viewBox="0 0 540 100" height="100" preserveAspectRatio="none" aria-hidden="true">
    <defs>
      <linearGradient id="efBlue" x1="0" y1="0" x2="1" y2="0">
        <stop offset="0" stop-color="#0b6fb3"/><stop offset=".5" stop-color="#1b8fd2"/><stop offset="1" stop-color="#39b1ea"/>
      </linearGradient>
    </defs>
    <path d="M0 30 C160 8,320 56,540 4 L540 18 C320 70,160 22,0 42Z" fill="#9aa0a6"/>
    <path d="M0 42 C160 20,320 72,540 18 L540 100 L0 100Z" fill="url(#efBlue)"/>
  </svg>
  <div class="contact">
    1876 N. 52nd Court Linden, NE 68420<br>
    +1 55 210-4836 &nbsp; hello@k7digital.net<br>
    <span class="url">www.k7digital.net</span>
  </div>
</section>

<!-- Envelope back -->
<section class="piece envelope-back" aria-label="Envelope back">
  <svg class="folds" viewBox="0 0 540 234" preserveAspectRatio="none" aria-hidden="true">
    <path d="M0 234 L230 120 M540 234 L310 120" stroke="#dcdfe2" stroke-width="1.2" fill="none"/>
  </svg>
  <svg class="flap" viewBox="0 0 540 120" preserveAspectRatio="none" aria-hidden="true">
    <defs>
      <linearGradient id="ebBlue" x1="0" y1="0" x2="1" y2="0">
        <stop offset="0" stop-color="#0b6fb3"/><stop offset=".5" stop-color="#1b8fd2"/><stop offset="1" stop-color="#39b1ea"/>
      </linearGradient>
    </defs>
    <path d="M0 0 L540 0 L540 22 C460 34,360 46,300 96 C285 108,255 108,240 96 C180 46,80 34,0 22Z" fill="url(#ebBlue)"/>
  </svg>
  <div class="brand-block">
    <div class="brand"><span class="brand-dot"></span>K7 Digital</div>
  </div>
</section>

</body>
</html>
```